Web site for Life Coaching Consultant

I require a website for a life coaching business. I have a Velvo Hosting account which I set up last week. I will need to be able to add articles and testimonials. The design should communicate that KT Amber Lantern is there to help people breakdown personal barriers and that we are an advocate to help them achieve personal goals.
Updates

Reason: I have some designers just accepting my invitation to submit so to give them a few days to submit. I have been thrilled with the quality of the submissions Thank you.

Hi everyone

I am loving all your designs.  The only feedback I can get from people is that they feel that the runner makes the web page look like a personal coach rather than a life coach that helps people with relations, career, and personal road blocks.

Sorry                                   

Reason: Hi I have increased the deadline as there has been so many amazing designs and some of you have asked to fine tune your entries. I would like to take this opportunity to thank you all. It is going to be a tough decision. I have put a few more pictures on the project page hoping this will help

Hi I just wanted to thank you all for your great designs.  As I got so many good designs I have asked people to vote.  I will be in touch in the next day or 2.

Cheers

Target Market(s)

People with self esteem issues either woman or girls, people who want to goal set and need an advocate

Industry/Entity Type

Life Coaching

Colors
d2a4cc
e567a6

Requirements
Must have
• must have bio section, logo, articles page, affirmation section and testimonial page.

```html
<!DOCTYPE html>
<html lang="en">
<head>
<meta charset="utf-8">
<title>KT Amber Lantern – Life Coaching</title>
<link href="https://fonts.googleapis.com/css2?family=Source+Sans+3:wght@400;600;700&display=swap" rel="stylesheet">
<style>
:root{
  --pink:#e6196f;
  --pink-dark:#b5124f;
  --pink-deep:#a0104a;
  --ink:#333;
  --body:#555;
  --bg:#f8f7f8;
  --hero:#f2f0f1;
  --tile:#eeeded;
  --white:#fff;
}
*{margin:0;padding:0;box-sizing:border-box}
html,body{width:976px;height:1200px;overflow:hidden}
body{position:relative;background:var(--bg);font-family:"Source Sans 3",sans-serif;color:var(--body)}
.abs{position:absolute}
/* header */
.header{left:0;top:0;width:976px;height:70px;background:var(--white)}
.brand{left:128px;top:8px;display:flex;align-items:center;gap:10px}
.brand-mark{width:76px;height:76px;border-radius:50%;background:var(--pink);border:6px solid var(--white);box-shadow:0 0 0 1px #f3d0de}
.brand-name{font-size:26px;font-weight:700;color:var(--pink);margin-top:-36px}
.search{left:618px;top:22px;width:235px;height:29px;border:1px solid var(--pink);border-radius:3px;background:var(--white);display:flex}
.search span{flex:1;font-size:12px;color:var(--pink-dark);padding:6px 12px}
.search-btn{width:39px;background:var(--pink);display:flex;align-items:center;justify-content:center}
.navbar{left:0;top:70px;width:976px;height:36px;background:var(--pink)}
.phone{left:218px;top:79px;display:flex;align-items:center;gap:8px;color:var(--white);font-weight:600;font-size:13px}
.nav{left:377px;top:70px;height:36px;display:flex;list-style:none}
.nav li{color:var(--white);font-size:11.5px;line-height:36px;padding:0 16px}
.nav li.active{background:var(--pink-dark);padding:0 21px}
/* hero */
.hero{left:0;top:106px;width:976px;height:350px;background:var(--hero)}
.hero-bar{left:0;top:456px;width:976px;height:6px;background:var(--pink-dark)}
.hero-title{left:130px;top:232px;font-size:30px;font-weight:700;color:var(--pink);line-height:32px}
.hero-title span{display:block;padding-left:18px}
.hero-rule{left:140px;top:314px;width:236px;height:1px;background:var(--pink)}
.hero-text{left:169px;top:322px;font-size:11px;font-weight:700;color:var(--pink);line-height:18px}
.btn{display:inline-block;font-size:9px;font-weight:600;border-radius:2px;text-align:center}
.btn-start{left:340px;top:390px;width:93px;height:26px;line-height:26px;background:var(--pink);color:var(--white);font-size:11px;font-weight:700}
.arrow{width:50px;height:50px;border-radius:50%;display:flex;align-items:center;justify-content:center}
.arrow-prev{left:65px;top:256px;background:var(--pink)}
.arrow-next{left:861px;top:256px;border:1px solid var(--pink);background:transparent}
.hero-photo{left:524px;top:148px;width:452px;height:308px;background:linear-gradient(120deg,#f2eeee 0%,#e8d8d0 55%,#f3efee 100%);border-radius:120px 0 0 0}
.dots{left:791px;top:429px;display:flex;gap:4px}
.dots i{width:14px;height:14px;border-radius:50%;border:1px solid var(--pink-dark);background:var(--white)}
.dots i.on{background:var(--pink)}
/* topics */
.card{top:500px;width:170px}
.card-img{height:115px;border:1px solid #ddd;border-bottom:3px solid var(--pink)}
.card h3{font-size:16px;font-weight:600;color:var(--pink);margin-top:10px;padding-bottom:4px;border-bottom:1px solid var(--pink)}
.card p{font-size:9.5px;line-height:15.6px;margin-top:6px;height:94px}
.btn-line{width:70px;height:23px;line-height:21px;border:1px solid var(--pink);color:var(--pink);background:var(--white);margin-top:5px}
.btn-fill{width:70px;height:23px;line-height:23px;background:var(--pink);color:var(--white)}
.divider{left:0;top:812px;width:976px;height:1px;background:#cfcfcf}
/* welcome */
.welcome-title{left:122px;top:838px;font-size:19px;color:var(--ink)}
.welcome-title b{color:var(--pink);font-weight:600}
.welcome-img{left:122px;top:884px;width:171px;height:155px;border:1px solid #ccc;background:linear-gradient(160deg,#dfe5ea,#8d97a0 60%,#c9ced2)}
.welcome-text{left:310px;top:881px;width:320px;font-size:9.5px;line-height:15.6px}
.welcome-text p+p{margin-top:15px}
.welcome-btn{left:309px;top:1018px}
.aside-title{left:682px;top:838px;font-size:19px;color:var(--ink)}
.aside-rule{left:682px;top:867px;width:171px;height:1px;background:var(--pink)}
.articles{left:682px;top:872px;width:171px;list-style:none}
.articles li{height:23px;margin-bottom:3.4px;background:var(--tile);font-size:11px;line-height:23px;padding-left:30px;position:relative;color:var(--ink)}
.articles li svg{position:absolute;left:11px;top:7px}
.articles li.active{background:var(--pink);color:var(--white);font-weight:600}
/* footer */
.footer{left:0;top:1110px;width:976px;height:66px;background:var(--pink)}
.footer-bar{left:0;top:1176px;width:976px;height:24px;background:var(--pink-deep)}
.footer-mark{left:130px;top:1092px;width:60px;height:60px;border-radius:50%;background:var(--pink);border:4px solid var(--white)}
.footer-name{left:110px;top:1148px;font-size:15px;font-weight:700;color:var(--white)}
.contact{left:246px;top:1118px;font-size:11px;color:var(--white);line-height:17.5px}
.contact td:first-child{width:48px}
.social{left:736px;top:1132px;display:flex;gap:7px}
.social i{width:24px;height:24px;border-radius:50%;background:var(--white)}
.copy{left:122px;top:1181px;font-size:9px;font-weight:600;color:var(--white)}
</style>
</head>
<body>
<header>
  <div class="abs header"></div>
  <div class="abs navbar"></div>
  <div class="abs brand"><div class="brand-mark"></div><div class="brand-name">Amber Lantern</div></div>
  <div class="abs search"><span>Search here....</span><div class="search-btn">
    <svg width="14" height="14" viewBox="0 0 14 14"><circle cx="6" cy="6" r="4.2" fill="none" stroke="#fff" stroke-width="2"/><path d="M9 9l3.5 3.5" stroke="#fff" stroke-width="2.2" stroke-linecap="round"/></svg></div></div>
  <div class="abs phone"><svg width="10" height="16" viewBox="0 0 10 16"><rect x="1" y="1" width="8" height="14" rx="1.5" fill="none" stroke="#fff" stroke-width="1.6"/><rect x="4" y="12" width="2" height="1.5" fill="#fff"/></svg>0400 123 456</div>
  <ul class="abs nav"><li class="active">Home</li><li>Life Coaching</li><li>Our Articles</li><li>Testimonials</li><li>About us</li><li>Contact</li></ul>
</header>

<section>
  <div class="abs hero"></div>
  <div class="abs hero-photo" role="img" aria-label="Smiling woman holding a sphere of positive thinking words"></div>
  <h1 class="abs hero-title">A Useful Guide to<span>Work Life Balance</span></h1>
  <div class="abs hero-rule"></div>
  <p class="abs hero-text">Lorem ipsum dolor sit amet, consectetur adipisicing<br>elit, sed do eiusmod tempor incididuntaliqua.</p>
  <a class="abs btn btn-start">START TODAY</a>
  <div class="abs arrow arrow-prev"><svg width="14" height="18" viewBox="0 0 14 18"><path d="M10 2L3 9l7 7" fill="none" stroke="#fff" stroke-width="3"/></svg></div>
  <div class="abs arrow arrow-next"><svg width="14" height="18" viewBox="0 0 14 18"><path d="M4 2l7 7-7 7" fill="none" stroke="#e6196f" stroke-width="3"/></svg></div>
  <div class="abs dots"><i class="on"></i><i></i><i></i><i></i></div>
  <div class="abs hero-bar"></div>
</section>

<section>
  <article class="abs card" style="left:122px"><div class="card-img" role="img" aria-label="Business team working at a laptop" style="background:linear-gradient(135deg,#9fb3c2,#3a3f4a)"></div><h3>Work &amp; Career</h3><p>Lorem ipsum dolor sit amet, consectetur adipisicing elit, sed do eiusmod tempor incididunt ut labore et dolore magna aliqua. Ut enim ad minim veniam, quis nostrud exercitation ullamco laboris nisi ut aliquip ex ea commodo consequat.</p><a class="btn btn-fill" style="display:block;margin-top:5px">Read more</a></article>
  <article class="abs card" style="left:309px"><div class="card-img" role="img" aria-label="Happy couple embracing in a kitchen" style="background:linear-gradient(135deg,#eef0f2,#b8a99a)"></div><h3>Love &amp; Relationships</h3><p>Lorem ipsum dolor sit amet, consectetur adipisicing elit, sed do eiusmod tempor incididunt ut labore et dolore magna aliqua. Ut enim ad minim veniam, quis nostrud exercitation ullamco laboris nisi ut aliquip ex ea commodo consequat.</p><a class="btn btn-line" style="display:block">Read more</a></article>
  <article class="abs card" style="left:496px"><div class="card-img" role="img" aria-label="Family hugging outdoors in autumn" style="background:linear-gradient(135deg,#8a9a6a,#5a4a3a)"></div><h3>Home &amp; Family</h3><p>Lorem ipsum dolor sit amet, consectetur adipisicing elit, sed do eiusmod tempor incididunt ut labore et dolore magna aliqua. Ut enim ad minim veniam, quis nostrud exercitation ullamco laboris nisi ut aliquip ex ea commodo consequat.</p><a class="btn btn-line" style="display:block">Read more</a></article>
  <article class="abs card" style="left:682px"><div class="card-img" role="img" aria-label="Woman with raised arms at the beach" style="background:linear-gradient(180deg,#5a9ccf,#bcd7ea 60%,#3f7fa8)"></div><h3>Life &amp; Living</h3><p>Lorem ipsum dolor sit amet, consectetur adipisicing elit, sed do eiusmod tempor incididunt ut labore et dolore magna aliqua. Ut enim ad minim veniam, quis nostrud exercitation ullamco laboris nisi ut aliquip ex ea commodo consequat.</p><a class="btn btn-line" style="display:block">Read more</a></article>
  <div class="abs divider"></div>
</section>

<section>
  <h2 class="abs welcome-title">Welcome to our <b>KT Amber Lantern</b></h2>
  <div class="abs welcome-img" role="img" aria-label="Colleagues reviewing a folder together"></div>
  <div class="abs welcome-text">
    <p>Lorem ipsum dolor sit amet, consectetur adipisicing elit, sed do eiusmod tempor incididunt ut labore et dolore magna aliqua. Ut enim ad minim veniam, quis nostrud exercitation ullamco laboris nisi ut aliquip ex ea commodo consequat. Duis aute irure dolor in reprehenderit in voluptate velit esse cillum dolore eu fugiat nulla pariatur.</p>
    <p>Duis aute irure dolor in reprehenderit in voluptate velit esse cillum dolore eu fugiat nulla pariatur.</p>
  </div>
  <a class="abs btn btn-fill welcome-btn">Read more</a>

  <h2 class="abs aside-title">Self Help Articles</h2>
  <div class="abs aside-rule"></div>
  <ul class="abs articles">
    <li><svg width="7" height="10" viewBox="0 0 7 10"><path d="M1 1l4 4-4 4" fill="none" stroke="#444" stroke-width="1.8"/></svg>Past Predicts Future?</li>
    <li class="active"><svg width="7" height="10" viewBox="0 0 7 10"><path d="M1 1l4 4-4 4" fill="none" stroke="#fff" stroke-width="1.8"/></svg>The Time Of Your Life</li>
    <li><svg width="7" height="10" viewBox="0 0 7 10"><path d="M1 1l4 4-4 4" fill="none" stroke="#444" stroke-width="1.8"/></svg>How to Find Love</li>
    <li><svg width="7" height="10" viewBox="0 0 7 10"><path d="M1 1l4 4-4 4" fill="none" stroke="#444" stroke-width="1.8"/></svg>Self Test</li>
    <li><svg width="7" height="10" viewBox="0 0 7 10"><path d="M1 1l4 4-4 4" fill="none" stroke="#444" stroke-width="1.8"/></svg>Your True Purpose</li>
    <li><svg width="7" height="10" viewBox="0 0 7 10"><path d="M1 1l4 4-4 4" fill="none" stroke="#444" stroke-width="1.8"/></svg>Past Predicts Future?</li>
    <li><svg width="7" height="10" viewBox="0 0 7 10"><path d="M1 1l4 4-4 4" fill="none" stroke="#444" stroke-width="1.8"/></svg>The Time Of Your Life</li>
  </ul>
</section>

<footer>
  <div class="abs footer"></div>
  <div class="abs footer-bar"></div>
  <div class="abs footer-mark"></div>
  <div class="abs footer-name">Amber Lantern</div>
  <table class="abs contact">
    <tr><td>Phone:</td><td>0400 123 456</td></tr>
    <tr><td>Email:</td><td>hello@amberlantern.com.au</td></tr>
    <tr><td>Address:</td><td>PO Box 1200 Sandgate VIC 3017</td></tr>
  </table>
  <div class="abs social" aria-label="Social links"><i></i><i></i><i></i><i></i></div>
  <div class="abs copy">Copyrights © 2014 &nbsp;|&nbsp; Amber Lantern</div>
</footer>
</body>
</html>
```